Technology solutions catalog

Were looking for a catalogue to supplement our website and corporate branding.

Our website will give you a good understanding of our products and services as well as our theme.

Our base colour and logo is red, white and grey.

www.voltrane.com.au

The aim of the catalogue is to showcase our business IT services & solutions. This will be a mix of education about the new solutions available to small and medium business today and how these solutions can increase productivity.

We would also like tip sections

This isn't all about selling but also about educating SMB's of the new and exciting IT solutions available today and having them book a free consult with us to discuss further about how we can help the business.

Solutions and area's that the catalogue will need to cover include

Front Cover -
-About us section, with our business contact information (1st page)
- Introduction. (2nd page)
-Communication Solutions - this includes Email, IP phones and business IT networks (2 pages)
- Data & Storage solutions (2 pages)
- Hardware (1 pages)
- Business IT health check list (1 page)
- Services and support offering (2 pages)
- Software & Popular cloud solutions (2 pages)
- Website / E-commerce solutions (2 pages)
Back cover

Based on two pages per solution the whole catalogue will be around 14 pages.

We don't need any text content done. We would like Headings on pages including page numbers. Footer please.

We're looking for a template that we can have our designer finish off by adding in some further product and service image and text.

Thank you for your consideration

Target Market(s)

IT for small and medium businesses

Industry/Entity Type

Supplement

Requirements
Must have
• Size A4
• Design supplied in Adobe indesign so we can edit and add our text and content
• Clean design

```html
<!DOCTYPE html>
<html lang="en">
<head>
<meta charset="utf-8">
<title>Voltrane Catalogue – Business IT health check list</title>
<link rel="stylesheet" href="https://fonts.googleapis.com/css2?family=Lato:wght@300;400;700;900&display=swap">
<style>
  :root {
    --stage: #262626;
    --paper: #ffffff;
    --brand-red: #bb1f26;
    --body-grey: #6b6b6b;
    --footer-bg: #353535;
    --footer-text: #b9b9b9;
    --photo-light: #dfe7ef;
    --photo-mid: #a9bccd;
    --photo-dark: #6f7f8f;
  }
  * { box-sizing: border-box; margin: 0; padding: 0; }
  html, body {
    width: 984px; height: 1200px; overflow: hidden;
    background: var(--stage);
    font-family: "Lato", Arial, sans-serif;
  }
  .stage { position: relative; width: 984px; height: 1200px; }
  .stage-label {
    position: absolute; top: 52px; left: 0; width: 984px;
    text-align: center; color: #fff; font-weight: 900; font-size: 20px;
  }
  .page {
    position: absolute; left: 158px; top: 109px;
    width: 683px; height: 967px; background: var(--paper);
  }
  .header-band {
    position: absolute; left: 0; top: 51px; width: 497px; height: 28px;
    background: var(--brand-red);
  }
  .brand-name {
    position: absolute; left: 521px; top: 48px;
    font-weight: 900; font-size: 27px; color: var(--brand-red);
    letter-spacing: 0.2px;
  }
  .page-title {
    position: absolute; left: 45px; top: 146px;
    font-weight: 300; font-size: 42px; color: var(--brand-red);
    letter-spacing: -0.2px;
  }
  .hero-photo {
    position: absolute; left: 34px; top: 223px; width: 620px; height: 196px;
    background: linear-gradient(100deg, var(--photo-mid) 0%, var(--photo-light) 40%, var(--photo-light) 62%, var(--photo-dark) 100%);
  }
  .content-block { position: absolute; width: 289px; }
  .content-block h2 {
    font-weight: 700; font-size: 16px; color: var(--brand-red);
    line-height: 20px; margin-bottom: 3px;
  }
  .content-block p {
    font-weight: 400; font-size: 12px; line-height: 17.4px;
    color: var(--body-grey); text-align: justify; hyphens: auto;
  }
  .col-left { left: 34px; }
  .col-right { left: 365px; }
  .row-top { top: 458px; }
  .row-bottom { top: 688px; }
  .page-footer {
    position: absolute; left: 0; bottom: 0; width: 683px; height: 34px;
    background: var(--footer-bg);
    display: flex; justify-content: space-between; align-items: center;
    padding: 0 24px 0 19px;
    font-size: 12px; font-weight: 400; color: var(--footer-text);
  }
</style>
</head>
<body>
<div class="stage">
  <div class="stage-label">Page 9</div>
  <article class="page">
    <div class="header-band"></div>
    <div class="brand-name">Voltrane</div>
    <h1 class="page-title">Business IT health check list</h1>
    <div class="hero-photo" role="img" aria-label="Photo of business reports with bar charts, a pen and glasses on a desk"></div>

    <section class="content-block col-left row-top">
      <h2>CONTENT TITLE</h2>
      <p>Lorem ipsum dolor sit amet, consectetuer adipiscing elit, sed diam nonummy nibh euismod tincidunt ut laoreet dolore magna aliquam erat volutpat. Ut wisi enim ad minim veniam, quis nostrud exerci tation ullamcorper suscipit lobortis nisl ut aliquip ex ea commodo consequat. Duis autem vel eum iriure dolor in hendrerit in vulputate velit esse molestie consequat, vel illum dolore eu feugiat nulla facilisis at vero eros et accumsan et iusto odio dignissim qui.</p>
    </section>
    <section class="content-block col-right row-top">
      <h2>CONTENT TITLE</h2>
      <p>Lorem ipsum dolor sit amet, consectetuer adipiscing elit, sed diam nonummy nibh euismod tincidunt ut laoreet dolore magna aliquam erat volutpat. Ut wisi enim ad minim veniam, quis nostrud exerci tation ullamcorper suscipit lobortis nisl ut aliquip ex ea commodo consequat. Duis autem vel eum iriure dolor in hendrerit in vulputate velit esse molestie consequat, vel illum dolore eu feugiat nulla facilisis at vero eros et accumsan et iusto odio dignissim qui.</p>
    </section>
    <section class="content-block col-left row-bottom">
      <h2>CONTENT TITLE</h2>
      <p>Lorem ipsum dolor sit amet, consectetuer adipiscing elit, sed diam nonummy nibh euismod tincidunt ut laoreet dolore magna aliquam erat volutpat. Ut wisi enim ad minim veniam, quis nostrud exerci tation ullamcorper suscipit lobortis nisl ut aliquip ex ea commodo consequat. Duis autem vel eum iriure dolor in hendrerit in vulputate velit esse molestie consequat, vel illum dolore eu feugiat nulla facilisis at vero eros et accumsan et iusto odio dignissim qui.</p>
    </section>
    <section class="content-block col-right row-bottom">
      <h2>CONTENT TITLE</h2>
      <p>Lorem ipsum dolor sit amet, consectetuer adipiscing elit, sed diam nonummy nibh euismod tincidunt ut laoreet dolore magna aliquam erat volutpat. Ut wisi enim ad minim veniam, quis nostrud exerci tation ullamcorper suscipit lobortis nisl ut aliquip ex ea commodo consequat. Duis autem vel eum iriure dolor in hendrerit in vulputate velit esse molestie consequat, vel illum dolore eu feugiat nulla facilisis at vero eros et accumsan et iusto odio dignissim qui.</p>
    </section>

    <footer class="page-footer">
      <span class="page-number">Page 9</span>
      <span class="page-url">www.voltrane.com.au</span>
    </footer>
  </article>
</div>
</body>
</html>
```